Flyer / marketing email used to solicate work for specialized tree removal equipment.

I'm looking for a flyer for door to door and direct mail distributon. Please utilize as much of the following verbiage as possible...

Breaking news!¿the only 170' grapple crane in use in North American is coming to your neighborhood This revolutionary technology will be in your area for a limited time. Our equipment allows to us accomplish the most challenging tree scenarios with no climber, limited personnel, and amazing efficiency.

This innovation has completely changed the cost of hazardous removals. Call now to get the most competitive estimate yet.

This technology is so limited and in high demand that it can only be in your area for a short time before it has to move on. Get on the list today, it may be months before it makes another round to your neighborhood. ¿

Target Market(s)

Flyers will be delivered in a high end residential neighborhood. Distribution will be on heavy stock and via email.

Colors

Designer to choose colors to be used in the design.

Requirements
Must have
• My logo. Pictures of the crane equipment. Pictures of other tree equipment.
• I'd like a two sided 4" x 5.5" mailer.
• I have permissions to utilize content from the sample one fold flyers I have uploaded.
• I'd like a majority of the content of the Vortaclaw (aka. Plover tree sample). The light background of the 528 Trees sample.
• A "BLACK FRIDAY SALE" theme would be awesome.
Nice to have
• Old time breaking news headline married with a high tech innovative feel
• OR
• BLACK FRIDAY SALE theme.

```html
<!DOCTYPE html>
<html lang="en">
<head>
<meta charset="utf-8">
<title>Grapple Crane Mailer</title>
<link href="https://fonts.googleapis.com/css2?family=Barlow:wght@500;700;800&family=Fira+Sans+Extra+Condensed:ital,wght@1,800;1,900&display=swap" rel="stylesheet">
<style>
  :root {
    --canvas: #bcbdbf;
    --paper: #ffffff;
    --ember-dark: #1a0400;
    --ember: #6b1400;
    --flare: #ff4a00;
    --sky-light: #8fbdf4;
    --sky: #5f9fe6;
    --pine: #3f5a2c;
    --crane: #1f2a6a;
    --royal: #1b78c6;
    --navy: #2b3a92;
    --charcoal: #444446;
    --ink: #111111;
    --forest: #2f4a1e;
  }
  * { margin: 0; padding: 0; box-sizing: border-box; }
  html, body { width: 991px; height: 1200px; overflow: hidden; }
  body { background: var(--canvas); position: relative; font-family: "Barlow", sans-serif; }

  .side { position: absolute; left: 187px; width: 618px; height: 478px; overflow: hidden; }

  /* Front */
  .side--front {
    top: 114px;
    background:
      radial-gradient(ellipse 60% 4% at 50% 9%, rgba(255,190,120,.95), rgba(255,74,0,.6) 40%, transparent 100%),
      radial-gradient(ellipse 80% 60% at 50% 45%, #7a1800, var(--ember) 50%, var(--ember-dark) 100%);
  }
  .headline-kicker {
    position: absolute; top: 20px; left: 0; width: 100%; text-align: center;
    font-family: "Fira Sans Extra Condensed", sans-serif; font-style: italic; font-weight: 800;
    font-size: 46px; color: #fff; letter-spacing: .5px;
  }
  .photo-frame {
    position: absolute; left: 49px; top: 104px; width: 516px; height: 358px;
    border-radius: 23px; overflow: hidden; background: var(--paper);
  }
  .photo-frame .photo {
    position: absolute; left: 0; top: 0; width: 100%; height: 274px;
    background:
      radial-gradient(ellipse 30% 55% at 88% 70%, rgba(31,42,106,.95), rgba(31,42,106,.55) 55%, transparent 100%),
      radial-gradient(ellipse 38% 30% at 35% 42%, rgba(63,90,44,.75), rgba(63,90,44,.3) 60%, transparent 100%),
      radial-gradient(ellipse 22% 18% at 48% 72%, rgba(63,90,44,.5), transparent 100%),
      linear-gradient(160deg, #6c8fda 0%, var(--sky) 40%, var(--sky-light) 100%);
  }
  .alert-banner { position: absolute; left: 141px; top: 72px; width: 325px; height: 85px; }
  .alert-banner svg { position: absolute; inset: 0; }
  .alert-banner span {
    position: absolute; inset: 0; display: flex; align-items: center; justify-content: center;
    font-family: "Fira Sans Extra Condensed", sans-serif; font-style: italic; font-weight: 900;
    font-size: 86px; color: #e3e6ea; letter-spacing: 2px; padding-right: 6px;
  }
  .ticker { position: absolute; left: 0; top: 274px; width: 100%; height: 84px; display: flex; }
  .ticker .brand-box {
    width: 129px; height: 100%;
    background: linear-gradient(180deg, var(--royal), var(--navy));
    display: flex; align-items: center; justify-content: center; text-align: center;
    color: #fff; font-weight: 700; font-size: 13px; line-height: 1.15; padding: 0 10px;
  }
  .ticker .claim {
    padding: 10px 0 0 23px; font-weight: 800; font-size: 21.5px; line-height: 19.5px;
    color: var(--charcoal); text-transform: uppercase;
  }

  /* Back */
  .side--back { top: 609px; background: var(--paper); }
  .brand-lockup {
    position: absolute; left: 48px; top: 103px; width: 180px; display: flex; align-items: center; gap: 9px;
    color: var(--forest); font-weight: 700; font-size: 19px; line-height: 1.15;
  }
  .brand-lockup .dot { flex: 0 0 28px; height: 28px; border-radius: 50%; background: var(--forest); }
  .copy { position: absolute; left: 250px; top: 32px; width: 345px; color: var(--ink); }
  .copy p { font-weight: 500; font-size: 12.3px; line-height: 14.3px; }
  .copy h2 {
    margin: 14px 0 20px; font-weight: 800; font-size: 20.6px; line-height: 19px;
    color: var(--forest); text-transform: uppercase;
  }
  .photo-strip { position: absolute; left: 0; top: 246px; width: 100%; height: 143px; display: flex; }
  .photo-strip .photo--truck { width: 190px; background: linear-gradient(180deg, #7ea6d6, #8a8f6a 60%, #6a6b5e); }
  .photo-strip .photo--crane { flex: 1; background: linear-gradient(180deg, #3d5c86, #4f6a4a 55%, #5c5a52); }
  .cta-banner { position: absolute; left: 78px; top: 376px; width: 459px; height: 31px; }
  .cta-banner svg { position: absolute; inset: 0; }
  .cta-banner span {
    position: absolute; inset: 0; display: flex; align-items: center; justify-content: center;
    color: #fff; font-weight: 700; font-size: 13.6px; text-transform: uppercase;
  }
  .phone {
    position: absolute; left: 0; top: 410px; width: 100%; text-align: center;
    font-weight: 800; font-size: 56px; line-height: 1; color: var(--forest); letter-spacing: -1px;
  }
</style>
</head>
<body>
  <section class="side side--front">
    <div class="headline-kicker">BREAKING NEWS</div>
    <div class="photo-frame">
      <div class="photo" role="img" aria-label="Grapple crane arm reaching into a tall pine tree against a blue sky"></div>
      <div class="ticker">
        <div class="brand-box">Evergreen Hour Tree Co.</div>
        <div class="claim">The only 170' grapple<br>crane in use in North American<br>is coming to your neighborhood</div>
      </div>
    </div>
    <div class="alert-banner">
      <svg viewBox="0 0 325 85" preserveAspectRatio="none" aria-hidden="true">
        <defs>
          <linearGradient id="alertFill" x1="0" y1="0" x2="0" y2="1">
            <stop offset="0" stop-color="#1b78c6"/>
            <stop offset="1" stop-color="#2b3a92"/>
          </linearGradient>
        </defs>
        <polygon points="10,0 325,0 315,85 0,85" fill="url(#alertFill)"/>
      </svg>
      <span>ALERT</span>
    </div>
  </section>

  <section class="side side--back">
    <div class="brand-lockup"><span class="dot"></span><span>Evergreen Hour Tree Co.</span></div>
    <div class="copy">
      <p>This revolutionary technology will be in your area for a limited time. Our equipment allows to us accomplish the most challenging tree scenarios with no climber, limited personnel, and amazing efficiency.</p>
      <h2>This innovation has completely changed the cost of hazardous removals.</h2>
      <p>This technology is so limited and in high demand that it can only be in your area for a short time before it has to move on. Get on the list today, it may be months before it makes another round to your neighborhood.</p>
    </div>
    <div class="photo-strip">
      <div class="photo--truck" role="img" aria-label="Bucket truck and crane boom parked beside a house"></div>
      <div class="photo--crane" role="img" aria-label="Crane boom extending over a house roof toward trees"></div>
    </div>
    <div class="cta-banner">
      <svg viewBox="0 0 459 31" preserveAspectRatio="none" aria-hidden="true">
        <polygon points="14,0 459,0 445,31 0,31" fill="#fff"/>
        <polygon points="18,2 454,2 441,31 4,31" fill="#2f4a1e"/>
      </svg>
      <span>Call now to get the most competitive estimate yet</span>
    </div>
    <div class="phone">-555.OAKS.808-</div>
  </section>
</body>
</html>
```